So Says Milo

I need a book cover designed - 6 inches wide x 9 inches tall. I would like it to be predominantly black and white, with a big bold title as attached:
To Be
MILO
I have attached a black and white photo that I would like to cover the bottom half (or close to it) of the book, with the words: Life Lessons That Helped Build KTW, Pelter Ridge Dam, And Transform Quolvex & ZOVA TV
By Desmond Alvarek
The designs I've included here I don't particularly like, although I think you can see my general idea. He is a black and white man, so I have a back and white photo.
A big bold headline and not overly sized black and white

```html
<!DOCTYPE html>
<html lang="en">
<head>
<meta charset="UTF-8">
<title>So Says Milo — Book Cover</title>
<link rel="stylesheet" href="https://fonts.googleapis.com/css2?family=Bodoni+Moda:ital,opsz,wght@0,6..96,400;1,6..96,400&family=Poppins:wght@700;800&display=swap">
<style>
  :root {
    --cover-black: #050505;
    --ink-white: #ffffff;
    --portrait-high: #8a8a8a;
    --portrait-light: #5a5a5a;
    --portrait-mid: #2e2e2e;
    --portrait-low: #161616;
  }
  html, body {
    margin: 0;
    padding: 0;
    width: 800px;
    height: 1200px;
    overflow: hidden;
    background: var(--cover-black);
  }
  .cover {
    position: relative;
    width: 800px;
    height: 1200px;
    background: var(--cover-black);
    overflow: hidden;
    color: var(--ink-white);
  }
  .portrait {
    position: absolute;
    left: 0;
    top: 380px;
    width: 800px;
    height: 820px;
    background:
      radial-gradient(ellipse 200px 250px at 490px 350px, var(--portrait-high) 0%, var(--portrait-light) 40%, var(--portrait-mid) 75%, rgba(20,20,20,0) 100%),
      radial-gradient(ellipse 330px 260px at 520px 820px, var(--portrait-mid) 0%, var(--portrait-low) 60%, rgba(10,10,10,0) 100%),
      radial-gradient(ellipse 520px 480px at 480px 420px, #1c1c1c 0%, #101010 60%, rgba(5,5,5,0) 100%);
  }
  .title {
    position: absolute;
    left: 126px;
    top: 124px;
    margin: 0;
    font-weight: normal;
  }
  .title-lead {
    display: block;
    font-family: "Bodoni Moda", "Didot", serif;
    font-weight: 400;
    font-size: 78px;
    line-height: 1;
    letter-spacing: -1px;
  }
  .title-name {
    display: block;
    margin-top: -12px;
    font-family: "Poppins", "Arial Black", sans-serif;
    font-weight: 800;
    font-size: 166px;
    line-height: 1;
    letter-spacing: -4px;
  }
  .subtitle {
    position: absolute;
    left: 129px;
    top: 402px;
    margin: 0;
    font-family: "Bodoni Moda", "Didot", serif;
    font-style: italic;
    font-size: 33px;
    line-height: 57px;
    letter-spacing: -0.5px;
  }
  .byline {
    position: absolute;
    left: 129px;
    top: 1006px;
    margin: 0;
    font-size: 44px;
    line-height: 1;
  }
  .byline-by {
    font-family: "Bodoni Moda", "Didot", serif;
    font-weight: 400;
  }
  .byline-author {
    font-family: "Poppins", "Arial", sans-serif;
    font-weight: 700;
    letter-spacing: -0.5px;
  }
</style>
</head>
<body>
  <main class="cover">
    <div class="portrait" role="img" aria-label="Black and white head-and-shoulders portrait photograph of the author, lit from the side against a dark background"></div>
    <h1 class="title">
      <span class="title-lead">So Says</span>
      <span class="title-name">MILO</span>
    </h1>
    <p class="subtitle">
      Life Lessons That Helped<br>
      Build KTW, Pelter Ridge Dam,<br>
      And Transform Quolvex<br>
      &amp; ZOVA TV
    </p>
    <p class="byline"><span class="byline-by">By</span> <span class="byline-author">Desmond Alvarek</span></p>
  </main>
</body>
</html>
```